One Page Website for Personal Trainer in London

I have a logo and need a one page website designed around my branding. I am a freelance Personal Trainer based in London specialising in bodyweight training for men and women. I would like the site to be modern and clean but not overtly urban in design.
I need the following headings:
About Me
My Services
Events
Blog
I don't need them to be seperate pages but if they can link to further down the page that would be great.
Industry/Entity Type
Personal Trainer
Coding
Coded - Design and coding required
Number of Pages Required
1 page
Requirements
Must have
- I need the following headings:
- About Me
- My Services
- Events
- Blog
- mobile friendly formatting
- health and fitness related photography
- Colour scheme in keeping with my existing logo

```html
<!DOCTYPE html>
<html lang="en">
<head>
<meta charset="utf-8">
<title>Marlowe Grant Personal Training</title>
<link rel="stylesheet" href="https://fonts.googleapis.com/css2?family=Arimo:wght@400;700&display=swap">
<style>
:root{
  --orange:#f0901e;
  --black:#0b0b0b;
  --panel:#121212;
  --header:#1a1a1a;
  --footer:#232323;
  --white:#ffffff;
  --grey:#9a9a9a;
  --line:#3a3a3a;
}
*{margin:0;padding:0;box-sizing:border-box}
html,body{width:1200px;height:3742px;overflow:hidden;background:var(--black);font-family:"Arimo",Arial,sans-serif;color:var(--white)}
.page{position:relative;width:1200px;height:3742px}
.abs{position:absolute}

.site-header{left:0;top:0;width:1200px;height:82px;background:linear-gradient(180deg,#2a2a2a,#141414);z-index:2}
.brand{left:62px;top:14px}
.brand-name{font-size:36px;font-weight:700;color:var(--orange);line-height:40px;letter-spacing:0.5px}
.brand-tag{font-size:13px;color:var(--grey);letter-spacing:7px;margin-top:2px;padding-left:18px}
.nav a{position:absolute;top:42px;font-size:14px;font-weight:700;color:var(--orange);text-decoration:underline}

.hero{left:0;top:82px;width:1200px;height:841px;background:radial-gradient(ellipse at 50% 30%,#4a3526 0%,#231a14 30%,#0a0a0a 70%)}
.hero-title{left:157px;top:520px;font-size:60px;font-weight:400;letter-spacing:1px}
.hero-sub{left:159px;top:592px;font-size:25px;letter-spacing:1px}
.btn{display:flex;align-items:center;justify-content:center;gap:14px;background:var(--orange);color:var(--white);font-size:14px;text-decoration:none}
.hero-btn{left:157px;top:654px;width:188px;height:42px}

.band{left:0;width:1200px;background:var(--orange)}

.row{left:0;width:1200px;background:var(--panel)}
.copy{width:611px;text-align:center;display:flex;flex-direction:column;align-items:center;justify-content:center}
.copy h2{font-size:22px;font-weight:400;letter-spacing:2px;line-height:26px;margin-bottom:22px}
.copy p{width:420px;font-size:15.5px;line-height:21px;letter-spacing:1.3px}
.photo{width:564px}

.cta{left:0;top:2937px;width:1200px;height:581px;background:linear-gradient(180deg,#5a5450 0%,#3b3632 55%,#4a2a1e 100%)}
.cta-title{left:0;top:3158px;width:1200px;text-align:center;font-size:45px;letter-spacing:1px}
.cta-btn{left:516px;top:3248px;width:188px;height:46px}

.site-footer{left:0;top:3518px;width:1200px;height:224px;background:var(--footer);color:var(--grey);font-size:12px}
.foot-links{left:354px;top:80px;width:110px}
.foot-links a{display:block;height:32px;line-height:30px;color:var(--grey);text-decoration:none;border-bottom:1px solid var(--line);text-align:center}
.foot-hours{left:497px;top:80px;line-height:16px}
.foot-info{left:721px;top:80px;line-height:16px}
</style>
</head>
<body>
<div class="page">

<header class="site-header abs">
  <div class="brand abs">
    <div class="brand-name">Marlowe Grant</div>
    <div class="brand-tag">PERSONAL TRAINING</div>
  </div>
  <nav class="nav">
    <a href="#about" style="left:544px">About</a>
    <a href="#services" style="left:630px">Services</a>
    <a href="#events" style="left:728px">Events</a>
    <a href="#blog" style="left:826px">Blog</a>
    <a href="#contact" style="left:910px">Contact</a>
  </nav>
</header>

<section class="hero abs" role="img" aria-label="Photo of a muscular man from behind doing pull-ups on a gym rack"></section>
<h1 class="hero-title abs">Only the Best Fitness</h1>
<p class="hero-sub abs">no bounderies, no obstacles.</p>
<a class="btn hero-btn abs" href="#contact">Contact Marlowe
  <svg width="8" height="12" viewBox="0 0 8 12"><path d="M1 1l5 5-5 5" fill="none" stroke="#fff" stroke-width="1.6"/></svg></a>

<div class="band abs" style="top:928px;height:107px"></div>

<section id="about" class="row abs" style="top:1035px;height:599px">
  <div class="copy abs" style="left:0;top:0;height:599px">
    <h2>Meet Your Personal Trainer<br>Marlowe Grant</h2>
    <p>Lorem ipsum dolor sit amet, consectetur adipiscing elit. Aliquam bibendum ante ut velit venenatis venenatis. Quisque sagittis, tellus a vehicula ultrices, dolor nulla mollis lectus, vel euismod lacus est id arcu. Vestibulum molestie non est quis rhoncus. Aliquam imperdiet erat ac elit suscipit.</p>
  </div>
  <div class="photo abs" style="left:611px;top:0;height:599px;background:linear-gradient(180deg,#6b6a4a 0%,#8b7d5c 22%,#5b6f86 30%,#7f8fa0 55%,#b7aa98 75%,#cbbba6 100%)" role="img" aria-label="Photo of a woman in swimwear walking on a beach"></div>
</section>

<section id="services" class="row abs" style="top:1634px;height:594px">
  <div class="photo abs" style="left:47px;top:0;height:594px;background:radial-gradient(ellipse at 50% 55%,#6a6a6a 0%,#2a2a2a 45%,#050505 80%)" role="img" aria-label="Photo of dumbbells and a barbell on a gym floor"></div>
  <div class="copy abs" style="left:589px;top:0;height:594px">
    <h2>Services</h2>
    <p>Lorem ipsum dolor sit amet, consectetur adipiscing elit. Aliquam bibendum ante ut velit venenatis venenatis. Quisque sagittis, tellus a vehicula ultrices, dolor nulla mollis lectus, vel euismod lacus est id arcu. Vestibulum molestie non est quis rhoncus. Aliquam imperdiet erat ac elit suscipit.</p>
  </div>
</section>

<section id="events" class="row abs" style="top:2228px;height:592px">
  <div class="copy abs" style="left:0;top:0;height:592px">
    <h2>Events</h2>
    <p>Lorem ipsum dolor sit amet, consectetur adipiscing elit. Aliquam bibendum ante ut velit venenatis venenatis. Quisque sagittis, tellus a vehicula ultrices, dolor nulla mollis lectus, vel euismod lacus est id arcu. Vestibulum molestie non est quis rhoncus. Aliquam imperdiet erat ac elit suscipit.</p>
  </div>
  <div class="photo abs" style="left:611px;top:0;height:592px;background:radial-gradient(ellipse at 35% 40%,#5c6c78 0%,#2d3a44 45%,#101418 85%)" role="img" aria-label="Photo of a woman lifting a dumbbell"></div>
</section>

<div class="band abs" style="top:2820px;height:117px"></div>

<section id="contact" class="cta abs" role="img" aria-label="Photo of a woman training with suspension straps in a fitness studio"></section>
<h2 class="cta-title abs">READY TO TAKE CONTROL?</h2>
<a class="btn cta-btn abs" href="#contact">Contact Marlowe
  <svg width="8" height="12" viewBox="0 0 8 12"><path d="M1 1l5 5-5 5" fill="none" stroke="#fff" stroke-width="1.6"/></svg></a>

<footer id="blog" class="site-footer abs">
  <nav class="foot-links abs">
    <a href="#about">About</a>
    <a href="#services">Services</a>
    <a href="#events">Events</a>
    <a href="#blog">Blog</a>
  </nav>
  <div class="foot-hours abs">
    Monday: 5:00am - 11:00pm<br>Tuesday: 5:00am - 11:00pm<br>Wednesday: 5:00am - 11:00pm<br>Thursday: 5:00am - 11:00pm<br>Friday: 5:00am - 11:00pm<br>Saturday: 5:00am - 11:00pm<br>Sunday: 5:00am - 11:00pm
  </div>
  <div class="foot-info abs">
    © 2017 Studio Northfield<br>All rights reserved.<br><br>1(555)014-2273<br><br><br>48 Elm Row,<br>Lakeford, Oregon, 97002
  </div>
</footer>

</div>
</body>
</html>
```